Banner for construction site to identify developer

we need a 4 foot by 8 foot banner to hang on the fence of a residential townhome development in Phoenix, Arizona that identifies Tolvane Holdings as the company behind the development/project. Also needs to include the logo, phone number, and web address. Would like to stick with the blue colors provided in the attached logo. The blues should stay the same but the letters in the logo can change to another color if necessary. Feel free to use "Tolvane Holdings" in place of "Tolvane Holdings Group". Looking for use of colors/design to take up space so banner is not just text with a logo.

Target Market(s)

drive by traffic looking at the site

Industry/Entity Type

Real Estate

Colors
0054AA
0677BA
7BADD7
CADEEF
E8F1F8

Requirements
Must have
• company name, phone number and web address

```html
<!DOCTYPE html>
<html lang="en">
<head>
<meta charset="utf-8">
<title>Tolvane Holdings Group – Site Banner</title>
<link rel="stylesheet" href="https://fonts.googleapis.com/css2?family=Open+Sans:wght@700&family=Oswald:wght@600&display=swap">
<style>
  :root {
    --paper: #ffffff;
    --ink: #39393b;
    --sky-blue: #1ba8db;
    --band-blue: #1554a5;
    --on-band: #ffffff;
  }
  html, body {
    margin: 0;
    padding: 0;
    overflow: hidden;
    background: var(--paper);
  }
  .banner {
    position: relative;
    width: 1200px;
    height: 600px;
    background: var(--paper);
    overflow: hidden;
  }
  .brand-mark {
    position: absolute;
    left: 216px;
    top: 118px;
    width: 182px;
    height: 182px;
    background: var(--sky-blue);
  }
  .brand-name {
    margin: 0;
    font-family: "Open Sans", sans-serif;
    font-weight: 700;
    color: var(--ink);
    line-height: 1;
  }
  .brand-name__main {
    position: absolute;
    left: 426px;
    top: 234px;
    font-size: 72px;
    letter-spacing: -1px;
    white-space: nowrap;
  }
  .brand-name__sub {
    position: absolute;
    right: 190px;
    top: 312px;
    font-size: 62px;
    letter-spacing: -0.5px;
    white-space: nowrap;
  }
  .contact-band {
    position: absolute;
    left: 0;
    top: 455px;
    width: 1200px;
    height: 145px;
    background: var(--band-blue);
  }
  .contact-item {
    position: absolute;
    top: 0;
    height: 132px;
    display: flex;
    align-items: center;
    gap: 22px;
    color: var(--on-band);
    font-family: "Oswald", sans-serif;
    font-weight: 600;
    font-size: 54px;
    letter-spacing: 0.5px;
    line-height: 1;
    white-space: nowrap;
  }
  .contact-item--phone { left: 114px; }
  .contact-item--web { left: 558px; }
  .contact-icon {
    width: 66px;
    height: 66px;
    flex: none;
  }
</style>
</head>
<body>
  <main class="banner">
    <div class="brand-mark" aria-hidden="true"></div>
    <h1 class="brand-name">
      <span class="brand-name__main">Tolvane Holdings</span>
      <span class="brand-name__sub">Group</span>
    </h1>

    <footer class="contact-band">
      <div class="contact-item contact-item--phone">
        <svg class="contact-icon" viewBox="0 0 66 66" aria-hidden="true" fill="none" stroke="var(--on-band)" stroke-width="5" stroke-linecap="round" stroke-linejoin="round">
          <path d="M16 5 C10 8 4 14 4 20 C6 36 24 56 44 62 C50 60 56 55 62 50 L52 41 C50 40 47 40 46 42 L42 46 C32 42 24 34 20 24 L24 20 C26 18 26 16 25 14 Z"/>
          <path d="M36 6 C48 8 58 18 60 30"/>
          <path d="M36 17 C42 18 48 24 49 30"/>
        </svg>
        <span>480-555-0147</span>
      </div>
      <div class="contact-item contact-item--web">
        <svg class="contact-icon" viewBox="0 0 66 66" aria-hidden="true" fill="none" stroke="var(--on-band)" stroke-width="5" stroke-linecap="round" stroke-linejoin="round">
          <path d="M62 30 A29 29 0 1 0 34 62"/>
          <path d="M33 4 C22 16 22 48 33 62"/>
          <path d="M33 4 C42 14 44 26 44 34"/>
          <path d="M6 22 H58"/>
          <path d="M4 40 H30"/>
          <path d="M40 40 L46 62 L50 54 L58 50 Z" fill="var(--on-band)"/>
        </svg>
        <span>tolvaneholdings.com</span>
      </div>
    </footer>
  </main>
</body>
</html>
```